Website for International Non-Profit for Birth Parent Searching

Tulrok is a 501(c)(3) non-profit organization that helps Chinese adoptees search and reunite with birth families who were separated due the One Child Policy in China. We want to create a website that can link to an information database that allows website users to easily access information around search ads in an organized way; help connect families to professional searchers; provide resources for community support for adoptees and their families as they embark on a personal and emotional journey of finding birth family through support groups on social media and consultation/education on the searching process; and provide the opportunity for the adoptive community to give back through donations and volunteer opportunities. The final design should foster a sense of community and be easy navigable to access the multiple resources we provide to help families search for each other. We would like to see designs with red/black/white color schemes that are gentle, inviting, and family friendly to viewers. We would like to see some design layouts with Chinese themes, if possible.

```html
<!DOCTYPE html>
<html lang="en">
<head>
<meta charset="utf-8">
<title>Tulrok — Bringing &amp; Keeping Families Together</title>
<link href="https://fonts.googleapis.com/css2?family=PT+Serif:wght@700&family=Poppins:wght@400;500;600&display=swap" rel="stylesheet">
<style>
:root{
  --red:#d71f27;
  --ink:#1d1d1d;
  --text:#555;
  --muted:#8a8a8a;
  --soft:#f6f6f6;
  --footer:#ebebeb;
  --white:#fff;
}
*{margin:0;padding:0;box-sizing:border-box}
html,body{width:1200px;height:4573px;overflow:hidden}
body{position:relative;background:var(--white);font-family:"Poppins",sans-serif;color:var(--ink)}
.abs{position:absolute}
.serif{font-family:"PT Serif",serif;font-weight:700}
.red{color:var(--red)}
.btn{position:absolute;display:flex;align-items:center;justify-content:center;border-radius:30px;font-size:12px;font-weight:600;white-space:nowrap}
.btn-red{background:var(--red);color:var(--white);box-shadow:0 10px 20px rgba(215,31,39,.3)}
.btn-line{border:1.5px solid #333;color:var(--ink);font-weight:500}
.photo{position:absolute}
.label{position:absolute;font-size:17px;color:var(--red);width:100%;text-align:center}
.heading{position:absolute;width:100%;text-align:center;font-size:30px}

/* hero */
.hero{position:absolute;left:0;top:0;width:1200px;height:589px;background:linear-gradient(100deg,#f3efea 0%,#ece6de 35%,#e9c98b 62%,#e7b85a 80%,#d9d4cc 100%)}
.logo{font-family:"PT Serif",serif;font-weight:700;font-size:26px;color:var(--red)}
.nav a{position:absolute;top:20px;font-size:15px;color:var(--ink);text-decoration:none}
.hero-title{left:185px;top:160px;font-size:46px;line-height:53px}
.hero-text{left:185px;top:292px;font-size:14px;line-height:23px;color:#333}

/* about */
.about-text{left:698px;top:797px;width:320px;font-size:14px;line-height:25.4px;color:var(--text)}

/* children */
.children{position:absolute;left:0;top:1216px;width:1200px;height:989px;background:var(--soft)}
.child-photo{position:absolute;width:262px;height:255px}
.child-tag{position:absolute;width:240px;height:66px;background:var(--white);text-align:center;box-shadow:0 6px 16px rgba(0,0,0,.06)}
.child-tag b{display:block;font-size:18px;font-weight:500;margin-top:8px;color:var(--ink)}
.child-tag span{font-size:14px;color:var(--muted)}

/* featured */
.featured{position:absolute;left:0;top:2205px;width:1200px;height:486px;background:linear-gradient(90deg,#eceae8 0%,#e6e3e0 45%,#cfc6bc 65%,#9a8f86 85%,#d8d3ce 100%)}
.checks li{list-style:none;display:flex;align-items:center;gap:12px;font-size:15px;color:#333;height:33px}

/* testimonials */
.card{position:absolute;width:261px;height:315px;background:var(--white);box-shadow:0 8px 26px rgba(0,0,0,.07);padding:36px 34px 0}
.stars{color:#f5b400;font-size:13px;letter-spacing:1px}
.card p{margin-top:14px;font-size:14.5px;line-height:22.5px;color:var(--muted)}
.author{position:absolute;left:34px;top:243px;display:flex;align-items:center;gap:16px}
.avatar{width:40px;height:40px;border-radius:50%;background:linear-gradient(135deg,#c9bbb0,#5b4e47)}
.author b{display:block;font-size:15px;font-weight:500}
.author span{font-size:10px;color:#aaa}
.arrow{position:absolute;width:32px;height:32px;border-radius:50%;display:flex;align-items:center;justify-content:center}
.dot{position:absolute;width:6px;height:6px;border-radius:50%;background:#999}

/* volunteer */
.band{position:absolute;left:0;top:3346px;width:1200px;height:254px;background:linear-gradient(90deg,#2d2d2d 0%,#4a4a4a 45%,#5a5a5a 70%,#3d3d3d 100%)}

/* news */
.news-photo{position:absolute;width:262px;height:186px}
.news-meta{position:absolute;font-size:12px;color:#444;display:flex;justify-content:space-between;width:232px}
.news-title{position:absolute;width:240px;font-size:15px;line-height:21px;font-weight:500;color:var(--ink)}

/* footer */
.footer{position:absolute;left:0;top:4221px;width:1200px;height:352px;background:var(--footer)}
.f-title{position:absolute;top:85px;font-size:15px;font-weight:500}
.f-links a{position:absolute;font-size:12.5px;color:#666;text-decoration:none}
.f-desc{position:absolute;font-size:12.5px;line-height:19px;color:#666}
</style>
</head>
<body>

<section class="hero">
  <div class="photo" role="img" aria-label="Smiling young girl with a yellow headband playing with toy building blocks" style="left:560px;top:0;width:640px;height:589px;background:radial-gradient(ellipse at 55% 45%,#f1c278 0%,#e9b45e 35%,rgba(233,200,140,0) 75%)"></div>
  <div class="photo" role="img" aria-label="Colourful toy blocks on a table" style="left:170px;top:510px;width:320px;height:79px;background:linear-gradient(90deg,#f2a6d6,#b6ecc1,#f4a7d2);opacity:.8"></div>
  <div class="abs logo" style="left:185px;top:8px">Tulrok</div>
  <nav class="nav">
    <a style="left:437px">Home</a>
    <a style="left:505px">Search</a>
    <a style="left:580px">reunion stories</a>
    <a style="left:740px">About</a>
    <a style="left:809px">Contact</a>
  </nav>
  <div class="btn btn-red" style="left:927px;top:20px;width:88px;height:26px;font-size:11px;box-shadow:none">Search</div>
  <h1 class="abs serif hero-title">Bringing &amp; Keeping<br>Families <span class="red">Together</span></h1>
  <p class="abs hero-text">Helping Chinese adoptees search for and<br>reunite with their birth families.</p>
  <div class="btn btn-red" style="left:185px;top:371px;width:133px;height:51px">Start Search</div>
  <div class="btn btn-line" style="left:337px;top:371px;width:133px;height:51px">Contact Us</div>
</section>

<section>
  <div class="photo" role="img" aria-label="Young girl with a pink backpack" style="left:185px;top:662px;width:209px;height:435px;background:linear-gradient(160deg,#8a7a70,#c9b9aa 55%,#e7d1d3)"></div>
  <div class="photo" style="left:402px;top:825px;width:245px;height:310px;background:var(--white)"></div>
  <div class="photo" role="img" aria-label="Little girl in a pink dress holding a teddy bear" style="left:408px;top:831px;width:233px;height:298px;background:linear-gradient(170deg,#e2b98a,#efd6c2 50%,#f2c6d6)"></div>
  <div class="abs" style="left:698px;top:658px;font-size:17px;color:var(--red)">About Us</div>
  <h2 class="abs serif" style="left:698px;top:700px;font-size:30px;line-height:39px">Start Your <span class="red">Search</span><br>Journey With Us.</h2>
  <p class="abs about-text">We are a non-profit that helps adoptees separated by the One Child Policy find their birth families. We organise search ads, link families with professional searchers, offer support groups and guidance, and welcome all who wish to give back.</p>
  <div class="btn btn-red" style="left:698px;top:1005px;width:135px;height:46px">Contact us</div>
</section>

<section class="children">
  <svg class="abs" style="left:0;top:140px" width="1200" height="849" viewBox="0 0 1200 849" aria-hidden="true">
    <path d="M0 120 C150 60 300 180 450 120 S750 60 900 120 S1100 180 1200 110 V849 H0Z" fill="#f1f1f1"/>
    <path d="M0 700 C200 640 350 760 600 700 S1000 640 1200 700 V849 H0Z" fill="#eeeeee"/>
  </svg>
  <div class="label" style="top:82px">Meet The Adoptees</div>
  <h2 class="heading serif" style="top:110px">Are <span class="red">Searching</span> For Family</h2>
</section>
<div class="child-photo" role="img" aria-label="Girl with a pink hair bow on grass" style="left:185px;top:1408px;background:linear-gradient(160deg,#4f7a2e,#8fb257 60%,#c5d9a0)"></div>
<div class="child-photo" role="img" aria-label="Boy in a paper crown with arms raised" style="left:469px;top:1408px;background:linear-gradient(160deg,#ece8e2,#d9c9b5 60%,#5a4a40)"></div>
<div class="child-photo" role="img" aria-label="Girl with a flower crown among pink flowers" style="left:754px;top:1408px;background:linear-gradient(160deg,#c8477a,#e6a1b8 50%,#2f3a2a)"></div>
<div class="child-photo" role="img" aria-label="Girl in a white top in a shop" style="left:185px;top:1736px;background:linear-gradient(160deg,#6b6a54,#c9bfa9 55%,#f2e7d2)"></div>
<div class="child-photo" role="img" aria-label="Boy in a red cap by a wooden fence" style="left:469px;top:1736px;background:linear-gradient(160deg,#6d7479,#9aa1a4 55%,#2a3447)"></div>
<div class="child-photo" role="img" aria-label="Smiling girl indoors" style="left:754px;top:1736px;background:linear-gradient(160deg,#8a7156,#c8a98a 55%,#5d8f8e)"></div>
<div class="child-tag" style="left:196px;top:1629px"><b>Anli Wen</b><span>Born 2001</span></div>
<div class="child-tag" style="left:480px;top:1629px"><b>Tao Ruan</b><span>Born 1998</span></div>
<div class="child-tag" style="left:765px;top:1629px"><b>Qiyu Lan</b><span>Born 2003</span></div>
<div class="child-tag" style="left:196px;top:1958px"><b>Sen Bai</b><span>Born 1996</span></div>
<div class="child-tag" style="left:480px;top:1958px"><b>Liya Fu</b><span>Born 2000</span></div>
<div class="child-tag" style="left:765px;top:1958px"><b>Hexi Mo</b><span>Born 1999</span></div>
<div class="btn btn-red" style="left:533px;top:2079px;width:134px;height:51px">Explore All</div>

<section class="featured">
  <div class="photo" role="img" aria-label="Boy hugging a family member and smiling" style="left:560px;top:0;width:640px;height:486px;background:linear-gradient(90deg,rgba(207,198,188,0) 0%,#b8a391 40%,#8d7b6c 70%,#c9c2ba 100%)"></div>
  <div class="abs" style="left:183px;top:92px;font-size:17px;color:var(--red)">Featured Reunion</div>
  <h2 class="abs serif" style="left:185px;top:135px;font-size:36px;line-height:45px">Every Child Deserves<br>To Know <span class="red">Family.</span></h2>
  <ul class="abs checks" style="left:185px;top:239px">
    <li><svg width="14" height="11" viewBox="0 0 14 11"><path d="M1 6l4 4 8-9" fill="none" stroke="#2c9a3c" stroke-width="1.8"/></svg>Browse an organised database of search ads.</li>
    <li><svg width="14" height="11" viewBox="0 0 14 11"><path d="M1 6l4 4 8-9" fill="none" stroke="#2c9a3c" stroke-width="1.8"/></svg>Connect with professional searchers.</li>
    <li><svg width="14" height="11" viewBox="0 0 14 11"><path d="M1 6l4 4 8-9" fill="none" stroke="#2c9a3c" stroke-width="1.8"/></svg>Join support groups for adoptees.</li>
  </ul>
  <div class="btn btn-red" style="left:185px;top:363px;width:133px;height:45px">Contact Us</div>
</section>

<section>
  <div class="label" style="top:2762px">Testimonial</div>
  <h2 class="heading serif" style="top:2797px">Happy Reunited <span class="red">Family</span></h2>
  <div class="card" style="left:185px;top:2876px">
    <div class="stars">★★★★☆</div>
    <p>After years of waiting, the search team helped me find my birth mother. Their guidance made the journey feel less lonely.</p>
    <div class="author"><div class="avatar" role="img" aria-label="Portrait of Ruolan Qi"></div><div><b>Ruolan Qi</b><span>Adoptee</span></div></div>
  </div>
  <div class="card" style="left:467px;top:2876px">
    <div class="stars">★★★★☆</div>
    <p>The support group gave our family a place to share, ask questions and learn about the search process step by step.</p>
    <div class="author"><div class="avatar" role="img" aria-label="Portrait of Minyi Su"></div><div><b>Minyi Su</b><span>Adoptive Parent</span></div></div>
  </div>
  <div class="card" style="left:753px;top:2876px">
    <div class="stars">★★★★☆</div>
    <p>Posting our search ad in one organised place meant more people saw it. We are so grateful to this caring community.</p>
    <div class="author"><div class="avatar" role="img" aria-label="Portrait of Xinran Tu"></div><div><b>Xinran Tu</b><span>Birth Family</span></div></div>
  </div>
  <div class="arrow" style="left:121px;top:3016px;border:1px solid #999"><svg width="8" height="12" viewBox="0 0 8 12"><path d="M6 1L1 6l5 5" fill="none" stroke="#555" stroke-width="1.5"/></svg></div>
  <div class="arrow" style="left:1045px;top:3016px;background:var(--red)"><svg width="8" height="12" viewBox="0 0 8 12"><path d="M2 1l5 5-5 5" fill="none" stroke="#fff" stroke-width="1.5"/></svg></div>
  <div class="dot" style="left:563px;top:3259px;background:var(--red)"></div>
  <div class="dot" style="left:593px;top:3259px"></div>
  <div class="dot" style="left:616px;top:3259px"></div>
  <div class="dot" style="left:640px;top:3259px"></div>
</section>

<section class="band" role="img" aria-label="Black and white photo of smiling children">
  <div class="abs" style="left:185px;top:54px;font-size:14px;color:var(--white)">Join With Us</div>
  <h2 class="abs serif" style="left:185px;top:90px;font-size:36px;line-height:44px;color:var(--white)">Give a Helping Hand<br>To Searching Families</h2>
  <div class="btn" style="left:806px;top:101px;width:211px;height:59px;background:var(--white);color:var(--ink);font-size:15px;font-weight:500">Become A Volunteer</div>
</section>

<section>
  <div class="label" style="top:3670px">Useful Information</div>
  <h2 class="heading serif" style="top:3704px">Our Recent <span class="red">News</span></h2>
  <div class="news-photo" role="img" aria-label="Family sitting on steps together" style="left:185px;top:3786px;background:linear-gradient(160deg,#3e5a3a,#6f7b88 55%,#9aa4ad)"></div>
  <div class="news-photo" role="img" aria-label="Family sharing a meal" style="left:469px;top:3786px;background:linear-gradient(160deg,#efe6dc,#d9b39a 55%,#c9544e)"></div>
  <div class="news-photo" role="img" aria-label="Cupped hands holding coins and a small note" style="left:754px;top:3786px;background:linear-gradient(160deg,#2f3b4a,#6d7a8a 50%,#b49a85)"></div>
  <div class="news-meta" style="left:196px;top:3986px"><span>Date - 24.03.2021</span><span>03 Comment</span></div>
  <div class="news-meta" style="left:481px;top:3986px"><span>Date - 12.03.2021</span><span>07 Comment</span></div>
  <div class="news-meta" style="left:766px;top:3986px"><span>Date - 06.03.2021</span><span>19 Comment</span></div>
  <div class="news-title" style="left:196px;top:4014px">8 Steps To Writing A Clear Birth Family Search Ad.</div>
  <div class="news-title" style="left:481px;top:4014px">Our Top Tips For Parents Supporting A Child's Search.</div>
  <div class="news-title" style="left:766px;top:4014px">Volunteers Who Make a Difference Help</div>
  <div class="btn btn-red" style="left:533px;top:4095px;width:134px;height:51px">Explore All</div>
</section>

<footer class="footer">
  <div class="abs logo" style="left:185px;top:74px;font-size:22px">Tulrok</div>
  <p class="f-desc" style="left:185px;top:130px;width:200px">A non-profit helping adoptees and birth families find each other.</p>
  <div class="abs" style="left:185px;top:204px;display:flex;gap:14px">
    <span style="width:9px;height:9px;border-radius:50%;background:#333"></span>
    <span style="width:9px;height:9px;border-radius:50%;background:#333"></span>
    <span style="width:9px;height:9px;border-radius:50%;background:#333"></span>
    <span style="width:9px;height:9px;border-radius:50%;background:#333"></span>
  </div>
  <div class="f-title" style="left:508px">Quick Links</div>
  <div class="f-title" style="left:666px">Help</div>
  <div class="f-title" style="left:804px">Contact Us</div>
  <div class="f-links">
    <a style="left:508px;top:130px">Home</a>
    <a style="left:508px;top:160px">Search</a>
    <a style="left:508px;top:190px">Reunion stories</a>
    <a style="left:508px;top:220px">About</a>
    <a style="left:666px;top:130px">Testimonials</a>
    <a style="left:666px;top:160px">Contact us</a>
    <a style="left:666px;top:190px">Donate</a>
    <a style="left:666px;top:220px">Privacy policy</a>
  </div>
  <svg class="abs" style="left:804px;top:132px" width="12" height="14" viewBox="0 0 12 14"><path d="M6 13s-4.5-4.6-4.5-7.6a4.5 4.5 0 019 0C10.5 8.4 6 13 6 13z" fill="none" stroke="#666"/><circle cx="6" cy="5.5" r="1.5" fill="none" stroke="#666"/></svg>
  <p class="f-desc" style="left:838px;top:128px;width:190px">Serving adoptees and families around the world.</p>
  <svg class="abs" style="left:804px;top:187px" width="12" height="12" viewBox="0 0 12 12"><path d="M2 1h2.5l1 3-1.5 1a7 7 0 003 3l1-1.5 3 1V10a1 1 0 01-1 1A10 10 0 011 2a1 1 0 011-1z" fill="none" stroke="#666"/></svg>
  <p class="f-desc" style="left:838px;top:184px">+000 555 0142</p>
  <svg class="abs" style="left:804px;top:218px" width="13" height="10" viewBox="0 0 13 10"><rect x=".5" y=".5" width="12" height="9" fill="none" stroke="#666"/><path d="M.5 .5l6 5 6-5" fill="none" stroke="#666"/></svg>
  <p class="f-desc" style="left:838px;top:214px">hello@tulrok.org</p>
  <div class="abs" style="left:0;top:293px;width:1200px;text-align:center;font-size:11px;color:#888">Copyright © 2021 All rights reserved</div>
</footer>

</body>
</html>
```